Banner Design for Physiotherapy Business

I need a banner designed for a physiotherapy business. The word ‘Physiotherapy’ should be prominent at the top. I’ve attached a document outlining what text and a suggestion of a picture I’d like included. The photo I have suggested in the document won’t upload to plumvista though as the dimensions are too large. I am open to other photos being used though. I would like to see designs that use the colour orange (as seen in the example) or green preferrably. The dimensions need to be 841mm x 2055mm and provided in PDF, JPG, and PNG format and 300dpi in CMYK colour mode.

```html
<!DOCTYPE html>
<html lang="en">
<head>
<meta charset="utf-8">
<title>Physiotherapy Banner</title>
<link href="https://fonts.googleapis.com/css2?family=Roboto:wght@400;500;700;900&display=swap" rel="stylesheet">
<style>
  :root {
    --orange: #f07a1a;
    --orange-deep: #e5620c;
    --orange-light: #f6a23a;
    --amber: #fbb82e;
    --white: #ffffff;
    --ink: #3a3a3a;
    --member-blue: #1f97d4;
    --photo-top: #e9e4dc;
    --photo-bottom: #b9b1a6;
  }
  html, body {
    margin: 0;
    padding: 0;
    width: 1200px;
    height: 2940px;
    overflow: hidden;
    background: var(--white);
    font-family: "Roboto", Arial, sans-serif;
  }
  .banner {
    position: relative;
    width: 1200px;
    height: 2940px;
    background: var(--white);
    overflow: hidden;
  }
  .top-strip {
    position: absolute;
    left: 0; top: 0;
    width: 1200px; height: 16px;
    background: var(--orange);
  }
  .headline {
    position: absolute;
    left: 0; top: 70px;
    width: 1200px;
    margin: 0;
    text-align: center;
    font-size: 128px;
    font-weight: 900;
    letter-spacing: 2px;
    color: var(--orange);
    line-height: 1;
  }
  .hero-photo {
    position: absolute;
    left: 40px; top: 250px;
    width: 1120px; height: 1300px;
    background: linear-gradient(180deg, var(--photo-top) 0%, #d8d0c4 50%, var(--photo-bottom) 100%);
  }
  .wave {
    position: absolute;
    left: 0; top: 0;
    width: 1200px; height: 2940px;
  }
  .services-tag {
    position: absolute;
    left: 232px; top: 1500px;
    width: 736px; height: 200px;
    box-sizing: border-box;
    border: 6px solid var(--white);
    background: linear-gradient(90deg, var(--orange-deep) 0%, var(--amber) 50%, var(--orange-deep) 100%);
    display: flex;
    align-items: center;
    justify-content: center;
    text-align: center;
    color: var(--white);
    font-size: 62px;
    font-weight: 700;
    line-height: 1.15;
    box-shadow: 0 6px 14px rgba(0,0,0,0.18);
  }
  .treatments {
    position: absolute;
    left: 40px; top: 1730px;
    width: 1120px;
    margin: 0; padding: 0;
    list-style: none;
    color: var(--white);
    font-size: 42px;
    font-weight: 700;
    text-align: center;
  }
  .treatments .row {
    height: 90px;
    line-height: 90px;
    white-space: nowrap;
  }
  .treatments .item::before {
    content: "•";
    margin-right: 18px;
  }
  .treatments .item + .item { margin-left: 36px; }
  .treatments .note {
    display: block;
    font-size: 36px;
    line-height: 40px;
    margin-top: -22px;
    margin-bottom: 14px;
  }
  .contact-card {
    position: absolute;
    left: 48px; top: 2600px;
    width: 1104px; height: 250px;
    background: var(--white);
    display: flex;
    align-items: center;
  }
  .member-badge {
    width: 540px;
    padding-left: 40px;
    display: flex;
    align-items: center;
    gap: 28px;
    box-sizing: border-box;
  }
  .member-badge .dot {
    width: 130px; height: 130px;
    border-radius: 50%;
    background: var(--member-blue);
    flex: none;
  }
  .member-badge .name {
    color: var(--member-blue);
    font-size: 34px;
    font-weight: 500;
    line-height: 1.15;
  }
  .divider {
    width: 3px; height: 190px;
    background: #cfcfcf;
  }
  .appointment {
    padding-left: 36px;
    color: var(--ink);
  }
  .appointment h2 {
    margin: 0 0 8px;
    font-size: 44px;
    font-weight: 700;
    color: var(--orange);
    border-bottom: 3px solid var(--orange);
    padding-bottom: 6px;
  }
  .appointment p {
    margin: 0;
    font-size: 28px;
    font-weight: 700;
    line-height: 1.3;
    color: var(--orange-deep);
  }
  .appointment .phone {
    display: flex;
    align-items: center;
    gap: 14px;
    margin-top: 8px;
    font-size: 36px;
    color: var(--ink);
    font-weight: 500;
  }
  .bottom-band {
    position: absolute;
    left: 0; top: 2850px;
    width: 1200px; height: 90px;
    background: linear-gradient(90deg, var(--amber), #ffd25a, var(--amber));
  }
</style>
</head>
<body>
<div class="banner">
  <div class="top-strip"></div>
  <h1 class="headline">PHYSIOTHERAPY</h1>

  <div class="hero-photo" role="img" aria-label="Photo of a physiotherapist stretching a patient's arm as she lies on a treatment table"></div>

  <svg class="wave" viewBox="0 0 1200 2940" aria-hidden="true">
    <defs>
      <linearGradient id="panelFill" x1="0" y1="0" x2="0" y2="1">
        <stop offset="0" stop-color="#f28424"/>
        <stop offset="1" stop-color="#e8670f"/>
      </linearGradient>
    </defs>
    <path d="M0 1000 C 120 1260, 420 1420, 1200 1440 L1200 2940 L0 2940 Z" fill="#f6a23a" opacity="0.85"/>
    <path d="M0 1060 C 140 1320, 460 1470, 1200 1480 L1200 2940 L0 2940 Z" fill="url(#panelFill)"/>
    <path d="M0 1060 C 140 1320, 460 1470, 1200 1480" fill="none" stroke="#ffffff" stroke-width="6" opacity="0.7"/>
  </svg>

  <div class="services-tag">WHAT WE TREAT /<br>SERVICES</div>

  <ul class="treatments">
    <li class="row"><span class="item">Arthritis</span><span class="item">Back pain / Neck pain</span></li>
    <li class="row"><span class="item">Sciatic pain</span><span class="item">Sports injuries</span></li>
    <li class="row"><span class="item">Repetitive strain injuries</span></li>
    <li class="row"><span class="item">Post surgical management</span></li>
    <li><span class="note">(hip and knee arthroscopes, joint replacement surgery)</span></li>
    <li class="row"><span class="item">Shoulder pain and dysfunction</span><span class="item">Tennis elbow</span></li>
    <li class="row"><span class="item">Postural pain</span><span class="item">Workplace injuries</span></li>
    <li class="row"><span class="item">Motor vehicle accidents</span><span class="item">Clinical exercise</span></li>
    <li class="row"><span class="item">Women's health issues</span></li>
    <li class="row"><span class="item">Pre-employment functional assessments</span></li>
  </ul>

  <div class="contact-card">
    <div class="member-badge">
      <span class="dot"></span>
      <span class="name">ALLIED PHYSIO<br>NETWORK<br>Member</span>
    </div>
    <div class="divider"></div>
    <div class="appointment">
      <h2>MAKE AN APPOINTMENT</h2>
      <p>Elmridge Family Practice</p>
      <p>18-20 Harlow Rd Elmridge VIC 3199</p>
      <div class="phone">
        <svg width="34" height="34" viewBox="0 0 24 24" aria-hidden="true">
          <circle cx="12" cy="12" r="11" fill="none" stroke="#f07a1a" stroke-width="2"/>
          <path d="M8.5 6.5l2 2-1.2 1.6c.7 1.6 2 2.9 3.6 3.6l1.6-1.2 2 2-1.3 1.8c-4-.4-7.7-4.1-8.1-8.1z" fill="#f07a1a"/>
        </svg>
        <span>(03) 9000 4417</span>
      </div>
    </div>
  </div>

  <div class="bottom-band"></div>
</div>
</body>
</html>
```